Truck wrap Design For KV CLEANERS

Create unique and eye catching design with provide logo and information.
Also Add Cartoon or silhouette of a men with vacuum or steam cleaner.
Please Use attached template.
It must include logo that is attached. and information below:
--555-314-2097
--www.kvrapidwashpro.example
--kvrapid@wavenetmail.example
-- NFTCB MASKS TEXTILE CLEANER

Services:

Carpet, upholstery, Air duct, Dryer vent, Hard surface cleaning,

Residential/Commercial Services.

Target Market(s)

everyone

Colors

Designer to choose colors to be used in the design.

Requirements
Must have
• All the information that is provide in descricption
Should not have
• silly background.

```html
<!DOCTYPE html>
<html lang="en">
<head>
<meta charset="utf-8">
<title>KV Cleaners – Truck Wrap</title>
<link rel="stylesheet" href="https://fonts.googleapis.com/css2?family=Oswald:wght@500&family=Roboto+Condensed:wght@700&family=Arimo:ital,wght@0,700;1,700&family=PT+Serif:wght@400&family=Roboto:wght@700&display=swap">
<style>
  :root{
    --canvas:#eef1f4;
    --blue-deep:#0a5fc0;
    --blue-mid:#2a8ee0;
    --blue-light:#9fd3f5;
    --ribbon-a:#f7a750;
    --ribbon-b:#fbc98a;
    --badge:#27b12a;
    --badge-dark:#138a18;
    --pill:#1550d6;
    --pill-dark:#0b2f9a;
    --tick:#2fb52f;
    --ink:#111;
    --navy:#0d1d52;
    --white:#fff;
    --door:#fbfbfb;
    --man-tones:linear-gradient(180deg,#9c4a2c 0%,#8ecbf0 30%,#2e8a78 70%,#1c6b57 100%);
    --vac-tones:linear-gradient(160deg,#64e25b,#1fa42c);
  }
  *{box-sizing:border-box;margin:0;padding:0}
  html,body{width:1200px;height:1200px;overflow:hidden;background:var(--canvas)}
  .canvas{position:relative;width:1200px;height:1200px}
  .side{position:absolute;left:30px;width:1140px;height:450px;display:flex;gap:20px}
  .side--driver{top:60px}
  .side--passenger{top:650px}
  .door{width:240px;height:450px;background:var(--door);border:2px solid #d6d9de;border-radius:8px;
    display:flex;flex-direction:column;align-items:center;justify-content:center;gap:14px}
  .door__mark{display:flex;align-items:center;gap:10px}
  .door__dot{width:22px;height:22px;border-radius:50%;background:var(--pill)}
  .door__name{font:700 26px 'Roboto Condensed',sans-serif;color:var(--navy);letter-spacing:1px;white-space:nowrap}
  .door__tag{font:400 9px 'PT Serif',serif;color:var(--navy);text-align:center;width:180px}
  .panel{position:relative;width:880px;height:450px;overflow:hidden;
    background:linear-gradient(110deg,var(--blue-deep) 0%,var(--blue-mid) 45%,var(--blue-light) 75%,var(--blue-mid) 100%)}
  .panel__rays{position:absolute;inset:0}
  .ribbon{position:absolute;z-index:2;width:410px;height:84px;transform:rotate(-3deg);
    background:linear-gradient(90deg,var(--ribbon-a),var(--ribbon-b) 60%,var(--ribbon-a));
    display:flex;align-items:center;justify-content:center;
    font:700 58px 'Roboto Condensed',sans-serif;color:var(--ink);letter-spacing:1px;white-space:nowrap}
  .cert{position:absolute;z-index:2;height:42px;padding:0 16px;border-radius:3px;
    background:linear-gradient(180deg,var(--badge),var(--badge-dark));
    display:flex;align-items:center;justify-content:center;white-space:nowrap;
    font:500 22px 'Oswald',sans-serif;color:var(--white)}
  .web{position:absolute;z-index:2;white-space:nowrap;font:700 28px 'Arimo',sans-serif;color:var(--white);
    text-shadow:0 0 2px #000,0 0 2px #000,1px 1px 0 #000}
  .email{position:absolute;z-index:2;white-space:nowrap;font:italic 700 20px 'Arimo',sans-serif;color:var(--navy)}
  .illus{position:absolute;z-index:1}
  .illus--man{background:var(--man-tones);border-radius:120px 120px 10px 10px;opacity:.9}
  .illus--vacuum{background:var(--vac-tones);border-radius:60px 90px 10px 10px}
  .services{position:absolute;z-index:2;width:260px;top:22px;text-align:center}
  .services__title{font:700 30px 'Roboto',sans-serif;color:var(--ink);margin-bottom:18px}
  .services__list{list-style:none;display:flex;flex-direction:column;gap:38px}
  .service{display:flex;align-items:center;gap:10px}
  .service__pill{flex:1;height:28px;border-radius:6px;border:2px solid var(--pill-dark);
    background:linear-gradient(180deg,#2d6bf0,var(--pill));color:var(--white);white-space:nowrap;
    font:400 18px 'PT Serif',serif;display:flex;align-items:center;justify-content:center}
  .tick{width:28px;height:28px;flex:none}
  .side--driver .services{right:20px}
  .side--driver .services__title{padding-left:30px}
  .side--passenger .services{left:20px}
  .side--passenger .services__title{padding-right:30px}
  .side--passenger .service{flex-direction:row-reverse}
</style>
</head>
<body>
<div class="canvas">

  <section class="side side--driver">
    <div class="door">
      <div class="door__mark"><span class="door__dot"></span><span class="door__name">KV CLEANERS</span></div>
      <p class="door__tag">A FRESH MODERN ANSWER TO AN AGE OLD CHORE</p>
    </div>
    <div class="panel">
      <svg class="panel__rays" width="880" height="450" viewBox="0 0 880 450">
        <path d="M560 0 L880 120 L880 0 Z" fill="#fff" opacity=".12"/>
        <path d="M620 450 L880 250 L880 450 Z" fill="#fff" opacity=".1"/>
        <path d="M430 450 Q360 200 480 60 Q540 10 620 0" fill="none" stroke="#d5ecfb" stroke-width="14" opacity=".7"/>
      </svg>
      <div class="ribbon" style="left:0;top:48px">555-314-2097</div>
      <div class="cert" style="left:10px;top:172px">NFTCB MASKS TEXTILE CLEANER</div>
      <div class="web" style="left:10px;top:250px">www.kvrapidwashpro.example</div>
      <div class="email" style="left:40px;top:296px">kvrapid@wavenetmail.example</div>
      <div class="illus illus--vacuum" role="img" aria-label="Cartoon green steam cleaner machine" style="left:0;top:345px;width:220px;height:105px"></div>
      <div class="illus illus--man" role="img" aria-label="Cartoon cleaning technician holding a vacuum hose" style="left:438px;top:8px;width:160px;height:442px"></div>
      <div class="services">
        <h2 class="services__title">Services:</h2>
        <ul class="services__list">
          <li class="service"><svg class="tick" viewBox="0 0 28 28"><circle cx="14" cy="14" r="13" fill="var(--tick)"/><path d="M8 14l4 4 8-8" fill="none" stroke="#fff" stroke-width="3"/></svg><span class="service__pill">Carpet Cleaning</span></li>
          <li class="service"><svg class="tick" viewBox="0 0 28 28"><circle cx="14" cy="14" r="13" fill="var(--tick)"/><path d="M8 14l4 4 8-8" fill="none" stroke="#fff" stroke-width="3"/></svg><span class="service__pill">Upholstery Cleaning</span></li>
          <li class="service"><svg class="tick" viewBox="0 0 28 28"><circle cx="14" cy="14" r="13" fill="var(--tick)"/><path d="M8 14l4 4 8-8" fill="none" stroke="#fff" stroke-width="3"/></svg><span class="service__pill">Air duct Cleaning</span></li>
          <li class="service"><svg class="tick" viewBox="0 0 28 28"><circle cx="14" cy="14" r="13" fill="var(--tick)"/><path d="M8 14l4 4 8-8" fill="none" stroke="#fff" stroke-width="3"/></svg><span class="service__pill">Dryer Vent</span></li>
          <li class="service"><svg class="tick" viewBox="0 0 28 28"><circle cx="14" cy="14" r="13" fill="var(--tick)"/><path d="M8 14l4 4 8-8" fill="none" stroke="#fff" stroke-width="3"/></svg><span class="service__pill">Hard surface Cleaning</span></li>
        </ul>
      </div>
    </div>
  </section>

  <section class="side side--passenger">
    <div class="panel">
      <svg class="panel__rays" width="880" height="450" viewBox="0 0 880 450">
        <path d="M0 0 L300 0 L0 110 Z" fill="#fff" opacity=".12"/>
        <path d="M0 450 L0 260 L260 450 Z" fill="#fff" opacity=".1"/>
        <path d="M560 450 Q480 250 530 130 Q570 60 660 40" fill="none" stroke="#d5ecfb" stroke-width="14" opacity=".7"/>
      </svg>
      <div class="services">
        <h2 class="services__title">Services:</h2>
        <ul class="services__list">
          <li class="service"><svg class="tick" viewBox="0 0 28 28"><circle cx="14" cy="14" r="13" fill="var(--tick)"/><path d="M8 14l4 4 8-8" fill="none" stroke="#fff" stroke-width="3"/></svg><span class="service__pill">Carpet Cleaning</span></li>
          <li class="service"><svg class="tick" viewBox="0 0 28 28"><circle cx="14" cy="14" r="13" fill="var(--tick)"/><path d="M8 14l4 4 8-8" fill="none" stroke="#fff" stroke-width="3"/></svg><span class="service__pill">Upholstery Cleaning</span></li>
          <li class="service"><svg class="tick" viewBox="0 0 28 28"><circle cx="14" cy="14" r="13" fill="var(--tick)"/><path d="M8 14l4 4 8-8" fill="none" stroke="#fff" stroke-width="3"/></svg><span class="service__pill">Air duct Cleaning</span></li>
          <li class="service"><svg class="tick" viewBox="0 0 28 28"><circle cx="14" cy="14" r="13" fill="var(--tick)"/><path d="M8 14l4 4 8-8" fill="none" stroke="#fff" stroke-width="3"/></svg><span class="service__pill">Dryer Vent</span></li>
          <li class="service"><svg class="tick" viewBox="0 0 28 28"><circle cx="14" cy="14" r="13" fill="var(--tick)"/><path d="M8 14l4 4 8-8" fill="none" stroke="#fff" stroke-width="3"/></svg><span class="service__pill">Hard surface Cleaning</span></li>
        </ul>
      </div>
      <div class="illus illus--man" role="img" aria-label="Cartoon cleaning technician holding a vacuum hose" style="left:292px;top:8px;width:160px;height:442px"></div>
      <div class="ribbon" style="right:0;top:58px">555-314-2097</div>
      <div class="cert" style="right:14px;top:182px">NFTCB MASKS TEXTILE CLEANER</div>
      <div class="web" style="right:14px;top:258px">www.kvrapidwashpro.example</div>
      <div class="email" style="right:40px;top:304px">kvrapid@wavenetmail.example</div>
      <div class="illus illus--vacuum" role="img" aria-label="Cartoon green steam cleaner machine" style="left:660px;top:350px;width:220px;height:100px;border-radius:90px 60px 10px 10px"></div>
    </div>
    <div class="door">
      <div class="door__mark"><span class="door__dot"></span><span class="door__name">KV CLEANERS</span></div>
      <p class="door__tag">A FRESH MODERN ANSWER TO AN AGE OLD CHORE</p>
    </div>
  </section>

</div>
</body>
</html>
```